Building Company Business Card Design

Need a design for a business card:
It needs to have: Name, Phone, Facebook link, Website, email
i would also like a list of works we undertake:
-New Homes
-Extensions, Renovations & Bathrooms
-Decking, Carports, Sheds (Residential and Industrial)
-Carpentry
-Fences, Patios & Pergolas

Contact Information for Business Card

Name, Phone, Facebook link, Website, email + details of services provided listed in description

```html
<!DOCTYPE html>
<html lang="en">
<head>
<meta charset="utf-8">
<title>Keystone Homes & Developments – Business Card</title>
<link rel="stylesheet" href="https://fonts.googleapis.com/css2?family=Montserrat:wght@400;500;600;700&family=Roboto+Condensed:wght@400;500&display=swap">
<style>
  :root{
    --stage:#2b2c2d;
    --card-dark:#1d1d1e;
    --pattern-a:#2a2a2b;
    --pattern-b:#4a4a4c;
    --paper:#ffffff;
    --ink:#1a1a1a;
    --ink-soft:#4a4a4a;
    --grey:#8c8c8c;
    --green:#3bb54a;
  }
  *{box-sizing:border-box;margin:0;padding:0}
  html,body{width:1200px;height:939px;overflow:hidden}
  body{background:var(--stage);position:relative;font-family:"Montserrat",sans-serif}

  .card{position:absolute;width:700px;height:400px;border-bottom:5px solid var(--green);box-shadow:0 14px 30px rgba(0,0,0,.45)}

  /* back side */
  .card--back{left:70px;top:40px;background:var(--card-dark);overflow:hidden}
  .back-pattern{position:absolute;inset:0;background:linear-gradient(120deg,var(--pattern-a) 0%,var(--card-dark) 45%,var(--pattern-b) 100%)}
  .back-brand{position:absolute;left:0;right:0;top:50%;transform:translateY(-50%);display:flex;align-items:center;justify-content:center;gap:14px}
  .back-brand__mark{width:26px;height:26px;background:var(--green)}
  .back-brand__name{font-weight:700;font-size:30px;color:#fff;letter-spacing:1px}

  /* front side */
  .card--front{left:430px;top:490px;background:var(--paper);color:var(--ink)}
  .brand{position:absolute;left:52px;top:118px;display:flex;align-items:center;gap:14px}
  .brand__mark{width:30px;height:30px;background:var(--green)}
  .brand__name{font-weight:700;font-size:25px;line-height:1.15;color:var(--ink);letter-spacing:.5px}

  .person{position:absolute;left:360px;top:40px}
  .person__name{font-weight:700;font-size:30px;letter-spacing:.5px;color:var(--grey)}
  .person__name span{color:var(--green)}
  .person__role{font-size:15px;color:var(--ink-soft);margin-top:2px;letter-spacing:1px}

  .address{position:absolute;left:360px;top:118px;font-size:15px;line-height:1.45;color:var(--ink-soft);letter-spacing:.8px}

  .contacts{position:absolute;left:360px;top:188px;list-style:none;font-size:15px;color:var(--ink);letter-spacing:.6px}
  .contacts li{display:flex;align-items:center;gap:9px;height:27px}
  .contacts li.social{margin-top:14px}
  .contacts svg{width:15px;height:15px;flex:none}
  .social-dot{width:15px;height:15px;border-radius:50%;background:var(--green);flex:none}

  .services{position:absolute;left:52px;top:250px;list-style:none;font-family:"Roboto Condensed",sans-serif;font-size:16px;color:var(--ink)}
  .services li{display:flex;align-items:baseline;gap:10px;height:25px}
  .services li::before{content:"";width:8px;height:8px;background:var(--green);flex:none;transform:translateY(-1px)}
  .services small{font-size:11px;color:var(--ink-soft)}
</style>
</head>
<body>

<section class="card card--back">
  <div class="back-pattern" role="img" aria-label="Repeating pattern of the company house mark in dark greys"></div>
  <div class="back-brand">
    <span class="back-brand__mark"></span>
    <span class="back-brand__name">Keystone Homes</span>
  </div>
</section>

<section class="card card--front">
  <div class="brand">
    <span class="brand__mark"></span>
    <span class="brand__name">KEYSTONE HOMES<br>&amp; DEVELOPMENTS</span>
  </div>

  <div class="person">
    <p class="person__name">SAM <span>CARTER</span></p>
    <p class="person__role">Owner</p>
  </div>

  <p class="address">12 Example Street,<br>Hillview, WA 6000</p>

  <ul class="contacts">
    <li>
      <svg viewBox="0 0 24 24" aria-hidden="true"><path fill="#3bb54a" d="M6.6 10.8a15.1 15.1 0 0 0 6.6 6.6l2.2-2.2c.3-.3.7-.4 1-.2 1.1.4 2.3.6 3.6.6.6 0 1 .4 1 1V20c0 .6-.4 1-1 1A17 17 0 0 1 3 4c0-.6.4-1 1-1h3.5c.6 0 1 .4 1 1 0 1.3.2 2.5.6 3.6.1.3 0 .7-.2 1z"/></svg>
      (08) 5550 1234
    </li>
    <li>
      <svg viewBox="0 0 24 24" aria-hidden="true"><rect x="2" y="5" width="20" height="14" fill="#3bb54a"/><path d="M2 5l10 8 10-8" fill="none" stroke="#fff" stroke-width="2"/></svg>
      hello@keystonehomes.example
    </li>
    <li>
      <svg viewBox="0 0 24 24" aria-hidden="true"><g fill="none" stroke="#3bb54a" stroke-width="2"><circle cx="12" cy="12" r="9"/><ellipse cx="12" cy="12" rx="4" ry="9"/><path d="M3 12h18M5 7h14M5 17h14"/></g></svg>
      www.keystonehomes.example
    </li>
    <li class="social">
      <span class="social-dot"></span>
      /keystonehomes
    </li>
  </ul>

  <ul class="services">
    <li>New Homes</li>
    <li>Extensions, Renovations &amp; Bathrooms</li>
    <li>Decking, Carports, Sheds <small>(Residential and Industrial)</small></li>
    <li>Carpentry</li>
    <li>Fences, Patios &amp; Pergolas</li>
  </ul>
</section>

</body>
</html>
```